Business card for sweet shop
Plumquistory
Project: Business card for sweet shop
Business card for sweet shop - Food
Creative Brief
Simple
korvenu_482@lunamail.test

```html
<!DOCTYPE html>
<html lang="en">
<head>
<meta charset="utf-8">
<title>Plumquistory business card</title>
<link href="https://fonts.googleapis.com/css2?family=Open+Sans:wght@400;600&display=swap" rel="stylesheet">
<style>
  :root {
    --backdrop: #e7e2dc;
    --frost: #f1eff0;
    --crimson: #c8144a;
    --crimson-deep: #a60e3c;
    --ink: #1a1416;
    --paper: #ffffff;
    --soft: #fbe6ec;
  }
  html, body {
    margin: 0;
    width: 1200px;
    height: 969px;
    overflow: hidden;
    background: var(--backdrop);
    font-family: "Open Sans", sans-serif;
  }
  .card {
    position: absolute;
    left: 120px;
    top: 214px;
    width: 960px;
    height: 540px;
    border-radius: 30px;
    overflow: hidden;
    background: var(--frost);
    box-shadow: 0 14px 40px rgba(60, 40, 40, 0.18);
  }
  .card-shapes { position: absolute; inset: 0; }
  .brand-mark {
    position: absolute;
    left: 132px;
    top: 229px;
    width: 136px;
    height: 136px;
    border-radius: 50%;
    background: var(--crimson);
  }
  .brand-name {
    position: absolute;
    left: 48px;
    top: 400px;
    margin: 0;
    font-size: 54px;
    font-weight: 600;
    color: var(--crimson);
    letter-spacing: -0.5px;
  }
  .contact {
    position: absolute;
    right: 58px;
    top: 62px;
    text-align: right;
    color: var(--paper);
  }
  .person-name { margin: 0; font-size: 32px; font-weight: 600; line-height: 1.2; }
  .person-role { margin: 2px 0 0; font-size: 22px; line-height: 1.3; }
  .address { margin: 22px 0 0; font-size: 20px; line-height: 31px; }
  .lines { list-style: none; margin: 14px 0 0; padding: 0; }
  .lines li {
    display: flex;
    justify-content: flex-end;
    align-items: center;
    gap: 18px;
    font-size: 20px;
    height: 38.5px;
    color: var(--soft);
  }
  .lines svg { width: 24px; height: 24px; flex: none; }
</style>
</head>
<body>
  <div class="card">
    <svg class="card-shapes" viewBox="0 0 960 540" width="960" height="540">
      <defs>
        <linearGradient id="crimsonFill" x1="0" y1="0" x2="1" y2="1">
          <stop offset="0" stop-color="var(--crimson)"/>
          <stop offset="1" stop-color="var(--crimson-deep)"/>
        </linearGradient>
      </defs>
      <path d="M330,0 Q600,270 430,540 L960,540 L960,0 Z" fill="url(#crimsonFill)"/>
    </svg>

    <div class="brand-mark"></div>
    <p class="brand-name">Plumquistory</p>

    <div class="contact">
      <p class="person-name">Dara Whitlow</p>
      <p class="person-role">Director</p>
      <p class="address">Suite 58 Orchard Lane<br>Velmont, Zip 4172, Arland</p>
      <ul class="lines">
        <li>214 608 3351
          <svg viewBox="0 0 24 24" fill="none" stroke="currentColor" stroke-width="2"><path d="M3 9c0-3 4-5 9-5s9 2 9 5v2h-5V8H8v3H3z"/><rect x="6" y="12" width="12" height="8" rx="1"/></svg>
        </li>
        <li>214 608 7720
          <svg viewBox="0 0 24 24" fill="none" stroke="currentColor" stroke-width="2"><rect x="7" y="2" width="10" height="20" rx="2"/><line x1="11" y1="18" x2="13" y2="18"/></svg>
        </li>
        <li>214 608 1946
          <svg viewBox="0 0 24 24" fill="none" stroke="currentColor" stroke-width="2"><circle cx="12" cy="12" r="9"/></svg>
        </li>
        <li>plumquistory
          <svg viewBox="0 0 24 24" fill="none" stroke="currentColor" stroke-width="2"><rect x="4" y="4" width="16" height="16" rx="2"/></svg>
        </li>
        <li>korvenu_482@lunamail.test
          <svg viewBox="0 0 24 24" fill="none" stroke="currentColor" stroke-width="2"><rect x="3" y="6" width="18" height="12"/><path d="M3 6l9 7 9-7"/></svg>
        </li>
        <li>www.plumquistory.test
          <svg viewBox="0 0 24 24" fill="none" stroke="currentColor" stroke-width="1.8"><circle cx="12" cy="12" r="9"/><ellipse cx="12" cy="12" rx="4" ry="9"/><line x1="3" y1="12" x2="21" y2="12"/></svg>
        </li>
      </ul>
    </div>
  </div>
</body>
</html>
```